Solar energy proposal for homeowners

I am providing households with solar energy proposals, and I need a high-quality brochure that is packaged cleverly to attract the homeowner's attention. Take a look at the one page solar brochure that I have included to get an idea of text and content.

Target Market(s)

Residential Homeowners

Industry/Entity Type

Solar

Requirements
Must have
• High quality document

```html
<!DOCTYPE html>
<html lang="en">
<head>
<meta charset="UTF-8">
<title>Solvenna Energy – Solar For $0 Down</title>
<link href="https://fonts.googleapis.com/css2?family=Inter:wght@600;700;800&family=Poppins:wght@300;400&display=swap" rel="stylesheet">
<style>
:root{
  --green-a:#7fd955;
  --green-b:#b7e21c;
  --blue-a:#0a9ad6;
  --blue-b:#12bcca;
  --teal:#16b3c6;
  --ink:#050505;
  --body:#1d1d1d;
  --white:#ffffff;
  --rule:#c9c9c9;
}
*{margin:0;padding:0;box-sizing:border-box}
html,body{width:848px;height:1200px;overflow:hidden;background:var(--white)}
.brochure{position:relative;width:848px;height:1200px;overflow:hidden;font-family:"Inter",Arial,sans-serif;color:var(--ink)}
.hero-photo{position:absolute;left:0;top:0;width:848px;height:460px;
  background:linear-gradient(160deg,#6b3a2a 0%,#b0573a 22%,#e8c7a4 34%,#3c5f9c 52%,#1f3f78 75%,#14305f 100%)}
.brand{position:absolute;left:42px;top:30px;display:flex;align-items:center;gap:14px}
.brand-mark{width:34px;height:34px;background:var(--teal)}
.brand-name{font-family:"Poppins",sans-serif;font-weight:400;font-size:38px;color:var(--teal);letter-spacing:.5px;line-height:1}
.offer-panel{position:absolute;left:0;top:288px;width:520px;height:295px;
  background:linear-gradient(90deg,var(--green-a),var(--green-b));border-radius:0 105px 0 72px}
.offer-title{position:absolute;left:42px;top:318px;font-weight:700;font-size:52px;line-height:61px;letter-spacing:-.5px;color:var(--ink)}
.offer-title .price{color:var(--white);font-weight:800}
.offer-tagline{position:absolute;left:43px;top:530px;font-weight:700;font-size:16px;color:var(--ink)}
.call-panel{position:absolute;left:469px;top:449px;width:379px;height:210px;
  background:linear-gradient(90deg,var(--blue-a),var(--blue-b));border-radius:56px 0 0 0}
.call-icon{position:absolute;left:488px;top:476px;width:82px;height:82px;border-radius:50%;background:var(--white);display:flex;align-items:center;justify-content:center}
.call-label{position:absolute;left:579px;top:484px;font-weight:700;font-size:14.5px;color:var(--white);letter-spacing:.3px}
.call-number{position:absolute;left:578px;top:506px;font-weight:700;font-size:35px;color:var(--white);letter-spacing:-.3px;white-space:nowrap}
.content{position:absolute;left:0;top:583px;width:848px;height:617px;background:var(--white);border-radius:0 95px 0 0}
.section-head{position:absolute;display:flex;align-items:center;gap:9px;font-weight:700;font-size:28px;color:var(--ink);line-height:1;white-space:nowrap}
.section-head::before{content:"";width:19px;height:22px;background:linear-gradient(135deg,var(--blue-a),var(--teal));clip-path:polygon(0 0,100% 25%,100% 100%,0 75%)}
.about-head{left:42px;top:604px}
.about-text{position:absolute;left:42px;top:643px;width:382px;font-family:"Poppins",sans-serif;font-weight:300;font-size:14px;line-height:25.6px;letter-spacing:.45px;text-align:justify;color:var(--body)}
.why-box{position:absolute;left:475px;top:603px;width:331px;height:252px;
  background:linear-gradient(90deg,var(--green-a),var(--green-b));border-radius:72px 72px 0 72px}
.why-head{left:510px;top:625px;font-size:28px}
.why-list{position:absolute;left:508px;top:668px;list-style:none}
.why-list li{display:flex;align-items:center;gap:4px;font-weight:600;font-size:19.5px;height:33.3px;color:var(--ink);white-space:nowrap}
.why-list li svg{flex:none}
.service-head{left:40px;top:827px}
.grid-rule-h{position:absolute;left:43px;top:999px;width:762px;border-top:1px dashed var(--rule)}
.grid-rule-v{position:absolute;left:424px;top:880px;height:232px;border-left:1px dashed var(--rule)}
.grid-node{position:absolute;left:420px;top:995px;width:9px;height:9px;border-radius:50%;border:1.5px solid var(--green-a);background:var(--white)}
.service{position:absolute;width:300px}
.service h3{font-weight:700;font-size:17.5px;color:var(--teal);margin-bottom:7px;line-height:1.1;white-space:nowrap}
.service p{font-family:"Poppins",sans-serif;font-weight:300;font-size:13px;line-height:19.5px;letter-spacing:.3px;color:var(--body);white-space:nowrap}
.service.left{left:116px}
.service.right{right:114px;text-align:right}
.row1{top:887px}.row2{top:1033px}
.service-icon{position:absolute;width:56px;height:60px;display:flex;align-items:center;justify-content:center;background:linear-gradient(135deg,var(--blue-a),var(--blue-b))}
.service-icon.left{left:45px;clip-path:polygon(0 17%,100% 0,100% 83%,0 100%)}
.service-icon.right{left:749px;clip-path:polygon(0 0,100% 17%,100% 100%,0 83%)}
.icon-row1{top:888px}.icon-row2{top:1034px}
.footer{position:absolute;left:0;top:1142px;width:848px;height:58px;background:linear-gradient(90deg,var(--blue-a),var(--blue-b));border-radius:36px 36px 0 0;
  color:var(--white);font-weight:700;font-size:19px;letter-spacing:-.2px}
.footer-item{position:absolute;top:14px;display:flex;align-items:center;gap:8px;white-space:nowrap;line-height:30px}
.footer-phone{left:31px}
.footer-address{left:221px}
.footer-web{left:532px}
.footer-dot{flex:none;width:30px;height:30px;border-radius:50%;background:var(--white);display:flex;align-items:center;justify-content:center}
</style>
</head>
<body>
<main class="brochure">
  <div class="hero-photo" role="img" aria-label="Photo of blue solar panels on a terracotta tiled house roof in sunlight"></div>

  <div class="brand">
    <span class="brand-mark"></span>
    <span class="brand-name">Solvenna Energy</span>
  </div>

  <div class="offer-panel"></div>
  <h1 class="offer-title">Solar For <span class="price">$0</span><br>Down.No Liens.<br>No Kidding.</h1>
  <p class="offer-tagline">Power Your Future with Solvenna Energy</p>

  <div class="call-panel"></div>
  <div class="call-icon">
    <svg width="50" height="50" viewBox="0 0 24 24" fill="none">
      <path d="M6.6 3.5 9 6.2c.5.5.5 1.3 0 1.8L7.7 9.4c1.2 2.7 3.6 5.1 6.5 6.6l1.4-1.3c.5-.5 1.3-.5 1.8 0l2.6 2.4c.5.5.5 1.3 0 1.8l-1.6 1.7c-.8.8-2 1.1-3 .7C9 19.2 4.8 15 2.8 9.6c-.4-1 0-2.2.7-3L5 5c.5-.5 1.1-.5 1.6-1.5z" fill="#0a9ad6"/>
      <path d="M14 3.5a7 7 0 0 1 6.5 6.5M14 6.7a3.9 3.9 0 0 1 3.4 3.4" stroke="#0a9ad6" stroke-width="1.8" stroke-linecap="round"/>
    </svg>
  </div>
  <p class="call-label">CALL US TODAY</p>
  <p class="call-number">(555)014-2290</p>

  <section class="content"></section>

  <h2 class="section-head about-head">About Solvenna energy</h2>
  <p class="about-text">At Solvenna Energy, our mission is to make solar simple and accessible for everyone. No high-pressure sales-just the information you need to make a smart choice. With our solar rental program, you can lower your monthly energy costs and pay less than your current electricity bill.</p>

  <div class="why-box"></div>
  <h2 class="section-head why-head">Why Choose Us?</h2>
  <ul class="why-list">
    <li><svg width="18" height="18" viewBox="0 0 20 20"><path d="M10 0C10.8 7 13 9.2 20 10 13 10.8 10.8 13 10 20 9.2 13 7 10.8 0 10 7 9.2 9.2 7 10 0z" fill="#fff"/></svg>No financing, No liens</li>
    <li><svg width="18" height="18" viewBox="0 0 20 20"><path d="M10 0C10.8 7 13 9.2 20 10 13 10.8 10.8 13 10 20 9.2 13 7 10.8 0 10 7 9.2 9.2 7 10 0z" fill="#fff"/></svg>No down payment</li>
    <li><svg width="18" height="18" viewBox="0 0 20 20"><path d="M10 0C10.8 7 13 9.2 20 10 13 10.8 10.8 13 10 20 9.2 13 7 10.8 0 10 7 9.2 9.2 7 10 0z" fill="#fff"/></svg>No insurance costs</li>
    <li><svg width="18" height="18" viewBox="0 0 20 20"><path d="M10 0C10.8 7 13 9.2 20 10 13 10.8 10.8 13 10 20 9.2 13 7 10.8 0 10 7 9.2 9.2 7 10 0z" fill="#fff"/></svg>No long-term commitment</li>
    <li><svg width="18" height="18" viewBox="0 0 20 20"><path d="M10 0C10.8 7 13 9.2 20 10 13 10.8 10.8 13 10 20 9.2 13 7 10.8 0 10 7 9.2 9.2 7 10 0z" fill="#fff"/></svg>No maintenance costs</li>
  </ul>

  <h2 class="section-head service-head">Our Best Service</h2>

  <div class="grid-rule-h"></div>
  <div class="grid-rule-v"></div>
  <div class="grid-node"></div>

  <div class="service-icon left icon-row1">
    <svg width="26" height="30" viewBox="0 0 26 30" fill="none" stroke="#fff" stroke-width="2" stroke-linecap="round">
      <circle cx="13" cy="10" r="8"/><path d="M15.5 6.8c-.6-.8-1.6-1.1-2.5-1.1-1.4 0-2.5.7-2.5 1.9 0 2.6 5.2 1.4 5.2 4.2 0 1.2-1.2 2-2.7 2-1.1 0-2.1-.4-2.7-1.2M13 4.5v1.2M13 14v1.3"/><path d="M9 21l4 5 4-5M13 19v7"/>
    </svg>
  </div>
  <div class="service left row1">
    <h3>Affordable &amp; Transparent</h3>
    <p>Simple pricing, no hidden fees and a fixed<br>monthly rate lower than typical<br>energy bills.</p>
  </div>

  <div class="service right row1">
    <h3>Expert Installation</h3>
    <p>Certified professionals handle installation<br>maintenance, and repairs<br>end to end.</p>
  </div>
  <div class="service-icon right icon-row1">
    <svg width="28" height="28" viewBox="0 0 24 24" fill="none" stroke="#fff" stroke-width="2" stroke-linecap="round" stroke-linejoin="round">
      <path d="M14.7 6.3a4 4 0 0 0 5 5L21 13a7 7 0 0 1-8.5 1.5L6 21a2 2 0 0 1-3-3l6.5-6.5A7 7 0 0 1 11 3z"/>
    </svg>
  </div>

  <div class="service-icon left icon-row2">
    <svg width="26" height="32" viewBox="0 0 26 32" fill="none" stroke="#fff" stroke-width="2" stroke-linecap="round">
      <path d="M13 26s-8-8-8-14a8 8 0 0 1 16 0c0 6-8 14-8 14z"/><circle cx="13" cy="12" r="3.5"/><path d="M6 30h14"/>
    </svg>
  </div>
  <div class="service left row2">
    <h3>Local Expertise</h3>
    <p>Florida-based team that understands the<br>needs of Orlando and statewide<br>homeowners.</p>
  </div>

  <div class="service right row2">
    <h3>Eco-Friendly</h3>
    <p>Clean, renewable solar energy that<br>helps reduce your carbon<br>footprint.</p>
  </div>
  <div class="service-icon right icon-row2">
    <svg width="28" height="28" viewBox="0 0 24 24" fill="none" stroke="#fff" stroke-width="2" stroke-linecap="round" stroke-linejoin="round">
      <path d="M5 19c0-8 5-13 15-14 0 10-5 15-13 15"/><path d="M5 19l7-7"/>
    </svg>
  </div>

  <footer class="footer">
    <div class="footer-item footer-phone">
      <span class="footer-dot"><svg width="17" height="17" viewBox="0 0 24 24"><path d="M6.6 3.5 9 6.2c.5.5.5 1.3 0 1.8L7.7 9.4c1.2 2.7 3.6 5.1 6.5 6.6l1.4-1.3c.5-.5 1.3-.5 1.8 0l2.6 2.4c.5.5.5 1.3 0 1.8l-1.6 1.7c-.8.8-2 1.1-3 .7C9 19.2 4.8 15 2.8 9.6c-.4-1 0-2.2.7-3L5 5c.5-.5 1.1-.5 1.6-1.5z" fill="#0a9ad6"/></svg></span>
      <span>(555)014-2290</span>
    </div>
    <div class="footer-item footer-address">
      <span class="footer-dot"><svg width="16" height="18" viewBox="0 0 24 28"><path d="M12 27s-9-9-9-16a9 9 0 0 1 18 0c0 7-9 16-9 16z" fill="#0a9ad6"/><circle cx="12" cy="11" r="3.5" fill="#fff"/></svg></span>
      <span>123 Anywhere St., Any City</span>
    </div>
    <div class="footer-item footer-web">
      <span class="footer-dot"><svg width="18" height="18" viewBox="0 0 24 24" fill="none" stroke="#0a9ad6" stroke-width="1.8"><circle cx="12" cy="12" r="9"/><path d="M3 12h18M12 3c3 3 3 15 0 18M12 3c-3 3-3 15 0 18"/></svg></span>
      <span>www.solvennaenergy.com</span>
    </div>
  </footer>
</main>
</body>
</html>
```